Business Card Design

I need a business card design for my law office based in Pasadena, California. I am a sole practitioner and I specialize in business transaction and litigation, probate and estate planning, taxation law, corporate and business formation, immigration and real estate. I want something that is simple, yet stands out.

A friend helped to create a logo about 6 years ago. I am open to new ideas to changing the logo.

Industry/Entity Type

Business

Contact Information for Business Card

Law Offices of Dorvan L. Mabry
842 W. Larkspur Ave., Suite 319
Pasadena, CA 90287
Tel: 626-555-0174
Fax: 626-555-0139
Email: dmabry@dlmlegalgroup.example

Attorney: Dorvan L. Mabry

```html
<!DOCTYPE html>
<html lang="en">
<head>
<meta charset="utf-8">
<title>Law Offices of Dorvan L. Mabry – Business Card</title>
<link rel="stylesheet" href="https://fonts.googleapis.com/css2?family=Cinzel:wght@400&family=Roboto:wght@400;700&display=swap">
<style>
  :root {
    --backdrop: #3b3b3b;
    --card: #ffffff;
    --ink: #3f3c3d;
    --ink-dark: #222222;
    --muted: #6b6b6b;
    --band-light: #a9a9a9;
    --band-dark: #4a4748;
    --band-darker: #262626;
    --rule: #b5b5b5;
    --marker-light: #9a9a9a;
  }
  * { box-sizing: border-box; margin: 0; padding: 0; }
  html, body {
    width: 1200px; height: 800px; overflow: hidden;
    background: var(--backdrop);
  }
  .canvas { position: relative; width: 1200px; height: 800px; }
  .card {
    position: absolute; left: 350px; width: 499px; height: 286px;
    background: var(--card); overflow: hidden;
  }
  .card--front { top: 85px; }
  .card--back { top: 422px; }
  .card__band { position: absolute; left: 0; bottom: 0; width: 499px; height: 19px; display: block; }

  /* Front */
  .brand {
    position: absolute; left: 0; right: 0; top: 62px;
    text-align: center; color: var(--ink);
    font-family: "Cinzel", serif; font-weight: 400;
  }
  .brand__square {
    display: block; width: 40px; height: 40px; margin: 0 auto 26px;
    background: var(--ink);
  }
  .brand__kicker { display: block; font-size: 11px; letter-spacing: 6px; margin-bottom: 10px; }
  .brand__name { display: block; font-size: 34px; letter-spacing: 1px; line-height: 1; }

  /* Back */
  .spine { position: absolute; left: 49px; top: 0; width: 1.5px; height: 267px; background: var(--rule); }
  .marker { position: absolute; left: 50px; width: 0; height: 0;
    border-top: 6px solid transparent; border-bottom: 6px solid transparent; border-left: 8px solid var(--marker-light); }
  .marker--primary { border-left-color: var(--ink-dark); border-top-width: 8px; border-bottom-width: 8px; border-left-width: 10px; }
  .contact { position: absolute; left: 68px; font-family: "Roboto", sans-serif; color: var(--muted); }
  .contact__name { font-size: 16px; font-weight: 700; color: var(--ink-dark); line-height: 1.1; }
  .contact__role { font-size: 10px; margin-top: 2px; }
  .detail { position: absolute; left: 68px; width: 240px; font-family: "Roboto", sans-serif; font-size: 11.5px; color: var(--muted); line-height: 15px; }
  .detail__label { font-weight: 700; color: var(--ink-dark); font-size: 11.5px; }
  .detail__rule { width: 115px; border-bottom: 1px dotted var(--rule); margin-top: 4px; }
</style>
</head>
<body>
<main class="canvas">
  <section class="card card--front" aria-label="Card front">
    <div class="brand">
      <span class="brand__square" aria-hidden="true"></span>
      <span class="brand__kicker">Law Offices of</span>
      <span class="brand__name">Dorvan L. Mabry</span>
    </div>
    <svg class="card__band" viewBox="0 0 499 19" aria-hidden="true">
      <polygon points="0,0 290,0 277,19 0,19" fill="var(--band-light)"/>
      <polygon points="290,0 499,0 499,19 277,19" fill="var(--band-dark)"/>
    </svg>
  </section>

  <section class="card card--back" aria-label="Card back">
    <div class="spine"></div>
    <span class="marker marker--primary" style="top:57px"></span>
    <span class="marker" style="top:76px"></span>
    <span class="marker" style="top:129px"></span>
    <span class="marker" style="top:165px"></span>
    <span class="marker" style="top:201px"></span>

    <div class="contact" style="top:57px">
      <p class="contact__name">Dorvan L. Mabry</p>
      <p class="contact__role">Attorney</p>
    </div>

    <div class="detail" style="top:128px">
      <p class="detail__label">Phone</p>
      <p>Tel: 626-555-0174, Fax: 626-555-0139</p>
      <div class="detail__rule"></div>
    </div>
    <div class="detail" style="top:164px">
      <p class="detail__label">E-mail</p>
      <p>dmabry@dlmlegalgroup.example</p>
      <div class="detail__rule"></div>
    </div>
    <div class="detail" style="top:200px">
      <p class="detail__label">Location</p>
      <p>842 W. Larkspur Ave., Suite 319</p>
      <p>Pasadena, CA 90287</p>
    </div>

    <svg class="card__band" viewBox="0 0 499 19" aria-hidden="true">
      <polygon points="0,0 290,0 277,19 0,19" fill="var(--band-light)"/>
      <polygon points="290,0 499,0 499,19 277,19" fill="var(--band-darker)"/>
    </svg>
  </section>
</main>
</body>
</html>
```